Bright Harbor Family Club Business Card Project

We are a Minneapolis based discount club that caters to families with children. We need a business card that can be used to communicate our contact information to other businesses that may wish to offer discounts on our website.

Please use placeholders for contact information (i.e. John Doe, 123 Any Street, Any Town, etc.) and include spaces for the following: Full name, title, email, phone number, website, one line street address, city, state, and zip code.

Reason: I have extended the deadline because I had not intended the project to close so quickly.

Target Market(s)

Most of the time the business cards will be used in business to business situations. However, from time to time they may be distributed to our end customer, families with children.

Industry/Entity Type

Club

Font styles to use
Serif
Sans Serif
Other font styles liked:
• Open to suggestions

Requirements
Nice to have
• We might use the reverse side of the card as the design for our membership card.

```html
<!DOCTYPE html>
<html lang="en">
<head>
<meta charset="utf-8">
<title>Bright Harbor Family Club – Business Card</title>
<link href="https://fonts.googleapis.com/css2?family=Lato:wght@400;700;900&display=swap" rel="stylesheet">
<style>
  :root {
    --bg: #e6e7ea;
    --card-red: #c8232c;
    --card-dark: #2b2829;
    --card-yellow: #f0b21c;
    --text-light: #ffffff;
    --photo-top: #eef0f2;
    --photo-bottom: #c9b8a6;
  }
  html, body {
    margin: 0;
    padding: 0;
    width: 1200px;
    height: 840px;
    overflow: hidden;
    background: var(--bg);
    font-family: "Lato", sans-serif;
  }
  .sheet {
    position: relative;
    width: 1200px;
    height: 840px;
    display: flex;
    align-items: center;
    justify-content: center;
    gap: 60px;
  }
  .card {
    position: relative;
    width: 525px;
    height: 300px;
    overflow: hidden;
    box-shadow: 0 6px 18px rgba(0,0,0,0.18);
  }

  /* Front */
  .card-front { background: var(--card-red); }
  .front-dark {
    position: absolute;
    left: 0; top: 0;
    width: 100%;
    height: 200px;
    background: var(--card-dark);
    clip-path: polygon(0 0, 100% 0, 100% 78%, 0 59%);
  }
  .brand {
    position: absolute;
    left: 0; right: 0; top: 34px;
    display: flex;
    align-items: center;
    justify-content: center;
    gap: 8px;
    color: var(--card-yellow);
    font-weight: 900;
    font-size: 19px;
    letter-spacing: 0.3px;
  }
  .brand-dot {
    width: 12px; height: 12px;
    border-radius: 50%;
    background: var(--card-yellow);
  }
  .photo {
    position: absolute;
    left: 62px; top: 92px;
    width: 402px; height: 112px;
    background: linear-gradient(180deg, var(--photo-top), var(--photo-bottom));
    border: 4px solid var(--card-dark);
  }
  .contact {
    position: absolute;
    left: 22px; top: 218px;
    color: var(--text-light);
    font-size: 11.5px;
    line-height: 15px;
  }
  .contact b { font-weight: 700; }
  .person {
    position: absolute;
    right: 26px; bottom: 18px;
    color: var(--text-light);
    font-size: 11.5px;
  }
  .person-name { font-weight: 700; font-size: 15px; }

  /* Back */
  .card-back { background: var(--card-red); }
  .card-back svg { position: absolute; inset: 0; }
  .back-brand {
    position: absolute;
    left: 0; right: 0; top: 130px;
    display: flex;
    align-items: center;
    justify-content: center;
    gap: 8px;
    color: var(--card-yellow);
    font-weight: 900;
    font-size: 19px;
  }
</style>
</head>
<body>
<main class="sheet">

  <section class="card card-front" aria-label="Business card front">
    <div class="front-dark"></div>
    <div class="brand"><span class="brand-dot"></span>Bright Harbor Family Club</div>
    <div class="photo" role="img" aria-label="Photo of a smiling family with two children and a dog"></div>
    <div class="contact">
      48 Harbor Lane, Maplewood MN 55101<br>
      <b>tel:</b> 4820 1937 &nbsp;-&nbsp; <b>fax:</b> 4820 1938<br>
      <b>email:</b> john@brightharbor.com
    </div>
    <div class="person"><span class="person-name">John Doe</span> manager</div>
  </section>

  <section class="card card-back" aria-label="Business card back">
    <svg width="525" height="300" viewBox="0 0 525 300" aria-hidden="true">
      <polygon points="0,0 525,0 525,40 90,40 90,300 0,300" fill="var(--card-yellow)"/>
      <polygon points="90,40 525,40 525,70 440,70 440,255 90,255" fill="var(--card-dark)"/>
      <rect x="90" y="255" width="435" height="45" fill="var(--card-red)"/>
      <rect x="440" y="70" width="85" height="230" fill="var(--card-red)"/>
    </svg>
    <div class="back-brand"><span class="brand-dot"></span>Bright Harbor Family Club</div>
  </section>

</main>
</body>
</html>
```